Young, dynamic furniture company needs a new business card design

We require a new business card design for our modern furniture company which supplies furniture and appliances to the property and development market.
Oakline Furnishings has become one of the leading furniture & appliance suppliers to the property market withing London. With over 10 years experience, we have increased our business to supply not only private landlords and managing agents, but also property developers, housing associations and local councils.
We offer not only a complete range of furniture which includes beds, wardrobes, dining sets and sofas, but also a high quality, full delivery and assembly service to help you with all our furnishing needs.

Target Market(s)

Private landlords, estate agents, letting agents, property management companies

Industry/Entity Type

Business

Contact Information for Business Card

Name,
Title,
Address,
Mobile,
Telephone,
Fax, Website, email address

Font styles to use
Sans Serif

Colors
3176b5
0555a3
85abd2
cfdeed

Requirements
Must have
• All the above information for each of our staff, along with our logo

```html
<!DOCTYPE html>
<html lang="en">
<head>
<meta charset="utf-8">
<title>Oakline Furnishings – Business Card</title>
<link href="https://fonts.googleapis.com/css2?family=Roboto:wght@300;400&family=Roboto+Condensed:wght@400&display=swap" rel="stylesheet">
<style>
  :root {
    --page-bg: #d9d6d2;
    --card-dark: #222023;
    --card-dark-soft: #2c2a2e;
    --card-light: #ffffff;
    --card-light-shade: #e9e9ea;
    --text-dark: #2a2a2c;
    --text-mid: #4a4a4e;
    --brand-blue: #3176b5;
    --brand-blue-deep: #0555a3;
    --brand-blue-soft: #85abd2;
    --white: #ffffff;
  }
  * { margin: 0; padding: 0; box-sizing: border-box; }
  html, body { width: 1200px; height: 1023px; overflow: hidden; }
  body {
    background: var(--page-bg);
    font-family: "Roboto", Arial, sans-serif;
    position: relative;
  }
  .card {
    position: absolute;
    left: 250px;
    width: 700px;
    height: 400px;
    border-radius: 14px;
    overflow: hidden;
    box-shadow: 0 10px 28px rgba(0,0,0,0.25);
  }

  /* ---------- Front ---------- */
  .card-front { top: 80px; background: linear-gradient(135deg, var(--card-light) 40%, var(--card-light-shade)); }
  .front-header {
    position: absolute; left: 0; top: 0; width: 100%; height: 104px;
    background: var(--card-dark);
    display: flex; align-items: center; padding-left: 40px; gap: 16px;
  }
  .brand-square { width: 38px; height: 38px; background: var(--brand-blue-deep); flex: none; }
  .brand-name {
    font-family: "Roboto Condensed", Arial, sans-serif;
    color: var(--white); font-size: 34px; line-height: 1; text-transform: uppercase; letter-spacing: 0.5px;
  }
  .brand-tagline {
    font-family: "Roboto Condensed", Arial, sans-serif;
    color: var(--white); font-size: 15px; text-transform: uppercase; margin-top: 4px; letter-spacing: 0.3px;
  }
  .front-footer {
    position: absolute; left: 0; bottom: 0; width: 100%; height: 22px; background: var(--card-dark);
  }
  .person { position: absolute; left: 60px; bottom: 66px; }
  .person-name { font-size: 38px; font-weight: 400; color: var(--text-dark); letter-spacing: 1px; }
  .person-title { font-size: 19px; color: var(--brand-blue); margin-top: 2px; }
  .divider {
    position: absolute; left: 365px; top: 150px; width: 1px; height: 210px;
    background: linear-gradient(to bottom, transparent, var(--brand-blue) 30%, var(--brand-blue) 70%, transparent);
  }
  .contact-list { position: absolute; left: 400px; top: 152px; list-style: none; }
  .contact-list li {
    display: flex; align-items: center; gap: 14px;
    font-size: 17px; font-weight: 300; color: var(--text-mid); letter-spacing: 1px; height: 38px;
  }
  .contact-list svg { width: 16px; height: 16px; flex: none; fill: var(--brand-blue); }

  /* ---------- Back ---------- */
  .card-back { top: 543px; background: var(--card-dark); }
  .back-band {
    position: absolute; left: 0; bottom: 0; width: 100%; height: 62px; background: var(--card-dark-soft);
    display: flex; align-items: center; justify-content: center;
    color: #bdbcc0; font-size: 16px; letter-spacing: 3px; font-weight: 300;
  }
  .back-rule { position: absolute; top: 36px; width: 1px; height: 240px; background: var(--brand-blue); }
  .back-rule.left { left: 70px; }
  .back-rule.right { right: 70px; }
  .back-brand {
    position: absolute; left: 0; top: 0; width: 100%; height: 338px;
    display: flex; align-items: center; justify-content: center; gap: 22px;
  }
  .back-brand .brand-square { width: 54px; height: 54px; background: var(--white); }
  .back-brand .brand-name { font-size: 46px; }
  .back-brand .brand-tagline { font-size: 19px; margin-top: 6px; }
</style>
</head>
<body>

<section class="card card-front" aria-label="Business card front">
  <header class="front-header">
    <span class="brand-square"></span>
    <div>
      <div class="brand-name">Oakline Furnishings</div>
      <div class="brand-tagline">Trade Furniture Solutions</div>
    </div>
  </header>

  <div class="person">
    <div class="person-name">Your Name</div>
    <div class="person-title">Title</div>
  </div>

  <div class="divider"></div>

  <ul class="contact-list">
    <li>
      <svg viewBox="0 0 16 16" aria-hidden="true"><path d="M3.6 1.5l2.2 2.6-1.3 1.6c.9 2 2.4 3.6 4.4 4.6l1.6-1.3 2.6 2.1-1.3 2.4C6.6 13.3 2.7 9.4 1.2 3l2.4-1.5z"/></svg>
      88-123-54320
    </li>
    <li>
      <svg viewBox="0 0 16 16" aria-hidden="true"><path d="M4.5 1h7a1 1 0 011 1v12a1 1 0 01-1 1h-7a1 1 0 01-1-1V2a1 1 0 011-1zm.5 2v9h6V3H5zm3 10a.8.8 0 100 1.6.8.8 0 000-1.6z"/></svg>
      88-123-54321
    </li>
    <li>
      <svg viewBox="0 0 16 16" aria-hidden="true"><path d="M4 1h6l2 2v3h1.5a1 1 0 011 1v7a1 1 0 01-1 1h-11a1 1 0 01-1-1V7a1 1 0 011-1H4V1zm1 1v4h6V3.5L9.5 2H5zm-1 7v1h2V9H4zm3 0v1h2V9H7zm3 0v1h2V9h-2zm-6 2v1h2v-1H4zm3 0v1h2v-1H7zm3 0v1h2v-1h-2z"/></svg>
      88-123-54322
    </li>
    <li>
      <svg viewBox="0 0 16 16" aria-hidden="true"><path d="M1 3h14v10H1V3zm1.6 1.2L8 8.6l5.4-4.4H2.6zM2.2 5.4v6.4h11.6V5.4L8 10.1 2.2 5.4z"/></svg>
      info@oaklinefurnishings.com
    </li>
    <li>
      <svg viewBox="0 0 16 16" aria-hidden="true"><path d="M8 1a5 5 0 015 5c0 3.6-5 9-5 9S3 9.6 3 6a5 5 0 015-5zm0 3a2 2 0 100 4 2 2 0 000-4z"/></svg>
      Your Address line1
    </li>
  </ul>

  <div class="front-footer"></div>
</section>

<section class="card card-back" aria-label="Business card back">
  <div class="back-rule left"></div>
  <div class="back-rule right"></div>
  <div class="back-brand">
    <span class="brand-square"></span>
    <div>
      <div class="brand-name">Oakline Furnishings</div>
      <div class="brand-tagline">Trade Furniture Solutions</div>
    </div>
  </div>
  <div class="back-band">www.oaklinefurnishings.com</div>
</section>

</body>
</html>
```